Zielgruppe
WIr sind ein klassisches Immobilienmaklerbüro für private Wohnimmobilien. Die Zielgruppe sind somit sowohl Verkäufer (i.d.R. gut situiert, 50-70 Jahre) als auch Käufer und Interessenten (20-35 Jahre).
Aufgabenstellung
Das Desgin soll seriös, vertrauenswürdig aber dennoch modern und dynamisch sein. Ich vollziehe aktuell einen Designwechsel und bin von einem schwarzen Design (www.wohn-punkt.example) auf ein helles Deisgn (http://wohnpunkt.de.xq48213.hostbeispiel.example/) umgestiegen. Die Visitenkarte soll zum neuen Design passen. Ein Bild von mir ist nicht gewünscht. Ob die Rückseite der Karten genutzt werden soll weiß ich selbst noch nicht. Wenn jemand eine sinnvolle Verwendung hat, bin ich dafür gerne offen.

```html
<!DOCTYPE html>
<html lang="de">
<head>
<meta charset="utf-8">
<title>WohnPunkt Visitenkarte</title>
<link rel="stylesheet" href="https://fonts.googleapis.com/css2?family=Arimo:wght@400;700&family=Tinos&display=swap">
<style>
  :root {
    --page: #e9e6e1;
    --card: #ffffff;
    --ink: #111111;
    --ink-soft: #444444;
    --leaf: #6fb120;
    --lime: #77ff0d;
    --title-green: #7ee41f;
    --sketch: #f3f3f3;
  }
  * { margin: 0; padding: 0; box-sizing: border-box; }
  html, body { width: 900px; height: 1200px; overflow: hidden; background: var(--page); }
  body { position: relative; font-family: "Arimo", Arial, sans-serif; color: var(--ink); }

  .card {
    position: absolute;
    width: 842px;
    height: 482px;
    background: var(--card);
    overflow: hidden;
    box-shadow: 0 6px 14px rgba(0,0,0,0.25);
  }
  .card-front { left: 25px; top: 88px; }
  .card-back { left: 29px; top: 646px; }

  .house-art {
    position: absolute;
    left: 131px; top: 65px;
    width: 550px; height: 250px;
    background: var(--sketch);
  }
  .swoosh { position: absolute; left: 0; top: 0; width: 842px; height: 482px; }

  .person { position: absolute; left: 40px; top: 74px; }
  .person-name {
    font-weight: 700; font-size: 40px; font-variant: small-caps;
    letter-spacing: 5px; line-height: 1;
  }
  .person-role {
    margin: 4px 0 0 35px;
    font-size: 24px; font-variant: small-caps; letter-spacing: 3px;
    color: var(--title-green); line-height: 1.1;
  }
  .person-degree {
    margin: 6px 0 0 55px;
    font-size: 19px; font-variant: small-caps; letter-spacing: 2.5px;
    color: var(--ink-soft);
  }

  .contact { position: absolute; top: 356px; font-weight: 700; font-variant: small-caps; line-height: 24px; }
  .contact-personal { left: 20px; font-size: 19px; letter-spacing: 2.6px; }
  .contact-company { left: 483px; font-size: 18px; letter-spacing: 3px; }

  .brand { position: absolute; left: 223px; top: 162px; display: flex; align-items: center; }
  .brand-name {
    font-size: 40px; font-variant: small-caps; letter-spacing: 6px;
    color: var(--ink); width: 300px;
  }
  .brand-square { width: 82px; height: 81px; background: var(--ink); margin-left: 12px; }

  .social-band { position: absolute; left: 0; top: 0; width: 842px; height: 482px; }
  .social { position: absolute; top: 358px; width: 200px; margin-left: -100px; text-align: center; }
  .social-dot { width: 52px; height: 52px; border-radius: 50%; background: var(--card); margin: 0 auto; }
  .social-label {
    font-family: "Tinos", "Times New Roman", serif;
    font-size: 26px; color: var(--card); margin-top: 4px;
  }
</style>
</head>
<body>
  <section class="card card-front">
    <div class="house-art" role="img" aria-label="Feine Linienzeichnung eines Wohnhauses"></div>
    <svg class="swoosh" viewBox="0 0 842 482" aria-hidden="true">
      <path d="M0 248 Q 330 490 841 154 Q 330 426 0 248 Z" fill="var(--leaf)"/>
    </svg>
    <div class="person">
      <h1 class="person-name">Jonas Reimer</h1>
      <p class="person-role">Geschäftsführer</p>
      <p class="person-degree">Betriebswirt (VWA)</p>
    </div>
    <div class="contact contact-personal">
      <p>Tel.: +49 7000 41526-23</p>
      <p>Fax: +49 7000 41526-24</p>
      <p>Mobil: +49 170 5558214</p>
      <p>Email: reimer@wohn-punkt.example</p>
    </div>
    <div class="contact contact-company">
      <p>info@wohn-punkt.example</p>
      <p>http://www.wohn-punkt.example</p>
      <p>WohnPunkt Immobilien GmbH</p>
      <p>Lindenweg 14, 73000 Musterstadt</p>
    </div>
  </section>

  <section class="card card-back">
    <div class="brand">
      <span class="brand-name">WohnPunkt</span>
      <span class="brand-square"></span>
    </div>
    <svg class="social-band" viewBox="0 0 842 482" aria-hidden="true">
      <rect x="0" y="312" width="842" height="170" fill="var(--lime)"/>
      <path d="M229 312 Q 418 350 607 312 Z" fill="var(--ink)"/>
    </svg>
    <div class="social" style="left:148px"><div class="social-dot"></div><p class="social-label">#news</p></div>
    <div class="social" style="left:434px"><div class="social-dot"></div><p class="social-label">#community</p></div>
    <div class="social" style="left:721px"><div class="social-dot"></div><p class="social-label">#chat</p></div>
  </section>
</body>
</html>
```